Growth-Bridge: Plus - EU-funded management consulting

A website to inform possible customers about my management consulting services for small and medium sized companies. I am using a funding for small and medium companies to do 10 days of workshops and coaching about leadership, further education and employee's health. The Funding is called "Wachstumsbrücke Plus" which means something like: Humans are the value of the company. The official logo is attached as a

Target Market(s)

Small and medium sized companies that want to improve their employee's well being and efficiency.

Industry/Entity Type

Management Consulting

Contact Information for Business Card

Veit Brosche, Kastanienweg 14, 10437 Berlin

Logo Text

WachstumsBrücke Plus - Beratung

Font styles to use
Serif
Sans Serif

Requirements
Must have
• a friendly and professional design
Nice to have
• saying somthing about: employees, leadership, further education and employees health are important to us.
Should not have
• should not be too shimmering

```html
<!DOCTYPE html>
<html lang="en">
<head>
<meta charset="utf-8">
<title>WachstumsBrücke Plus – Beratung</title>
<link href="https://fonts.googleapis.com/css2?family=Open+Sans:wght@300;400;600;700&display=swap" rel="stylesheet">
<style>
  :root {
    --teal: #1d8fbf;
    --band: #1f9bd3;
    --orange: #e57f2b;
    --label: #c86a1e;
    --ink: #333b44;
    --muted: #8a9199;
    --grey-bg: #efefef;
    --card-bg: #ffffff;
    --backdrop: #dcdcdc;
    --footer: #1d2a39;
    --footer-deep: #152130;
    --white: #ffffff;
  }
  * { box-sizing: border-box; margin: 0; padding: 0; }
  html, body { width: 709px; height: 1200px; overflow: hidden; }
  body { font-family: "Open Sans", Arial, sans-serif; color: var(--ink); background: var(--white); position: relative; }

  .site-header { position: absolute; top: 0; left: 0; width: 709px; height: 56px; }
  .brand { position: absolute; left: 28px; top: 12px; display: flex; align-items: center; gap: 7px; }
  .brand-mark { width: 18px; height: 18px; background: var(--teal); }
  .brand-name { font-size: 13px; font-weight: 600; color: var(--teal); letter-spacing: .2px; }
  .main-nav { position: absolute; right: 26px; top: 12px; display: flex; gap: 0; }
  .main-nav a { font-size: 6.5px; font-weight: 600; color: var(--teal); text-decoration: none; padding: 4px 12px; }
  .main-nav a.active { border-bottom: 2px solid var(--teal); }

  .hero { position: absolute; top: 59px; left: 28px; width: 653px; height: 206px; overflow: hidden; }
  .hero-photo { position: absolute; inset: 0; background: linear-gradient(120deg, #8d9cab 0%, #5f6f80 35%, #c4ccd4 60%, #46525f 100%); }
  .hero-shade { position: absolute; inset: 0; background: rgba(20,35,55,.25); }
  .hero-title { position: absolute; top: 66px; width: 100%; text-align: center; color: var(--white); font-size: 15.5px; font-weight: 700; }
  .hero-sub { position: absolute; top: 90px; width: 100%; text-align: center; color: var(--white); font-size: 6.5px; font-weight: 600; letter-spacing: .3px; }
  .hero-dots { position: absolute; right: 16px; bottom: 10px; display: flex; gap: 4px; }
  .hero-dots span { width: 7px; height: 7px; border-radius: 50%; background: var(--white); opacity: .7; }
  .hero-dots span.on { background: var(--orange); opacity: 1; }

  .section-title { text-align: center; color: var(--teal); font-size: 14px; font-weight: 700; letter-spacing: .4px; }
  .divider { display: block; margin: 3px auto 0; }

  .about { position: absolute; top: 277px; left: 0; width: 709px; height: 137px; background: var(--grey-bg); padding-top: 19px; }
  .about-text { width: 620px; margin: 8px auto 0; font-size: 6.5px; line-height: 10px; text-align: center; color: var(--muted); }

  .workshops { position: absolute; top: 414px; left: 0; width: 709px; height: 272px; padding-top: 6px; }
  .workshop { position: absolute; top: 47px; width: 160px; text-align: left; }
  .workshop svg { display: block; margin: 0 auto; }
  .workshop h3 { text-align: center; font-size: 10.5px; font-weight: 400; color: var(--label); margin-top: 14px; }
  .workshop p { font-size: 6px; line-height: 9px; color: var(--muted); margin-top: 5px; padding-left: 12px; }
  .read-more { display: inline-block; margin: 9px 0 0 12px; background: var(--orange); color: var(--white); font-size: 5.5px; padding: 2px 7px; border-radius: 2px; }

  .mission { position: absolute; top: 686px; left: 0; width: 709px; height: 130px; background: var(--band); }
  .mission-text { position: absolute; left: 34px; top: 36px; width: 430px; color: var(--white); font-size: 19px; font-weight: 300; line-height: 27px; }
  .mission-button { position: absolute; left: 485px; top: 42px; width: 128px; height: 30px; border: 2px solid var(--white); border-radius: 7px; color: var(--white); font-size: 15px; text-align: center; line-height: 26px; }

  .testimonials { position: absolute; top: 816px; left: 0; width: 709px; height: 241px; padding-top: 38px; }
  .testimonials .section-title { font-size: 13.5px; }
  .testimonials-intro { width: 400px; margin: 10px auto 0; text-align: center; font-size: 6px; line-height: 9px; color: var(--muted); }
  .testimonial-stage { position: absolute; top: 113px; left: 133px; width: 443px; height: 128px; background: var(--backdrop); }
  .testimonial { position: absolute; top: 10px; width: 124px; height: 118px; background: var(--card-bg); text-align: center; }
  .avatar { position: absolute; top: -12px; left: 47px; }
  .testimonial p { margin: 32px 10px 0; font-size: 5.5px; line-height: 8px; color: var(--muted); text-align: left; }
  .testimonial h4 { margin-top: 8px; font-size: 10px; font-weight: 400; color: var(--ink); }
  .testimonial span { display: block; font-size: 5.5px; color: var(--muted); }

  .site-footer { position: absolute; top: 1057px; left: 0; width: 709px; height: 126px; background: var(--footer); color: var(--white); }
  .footer-col { position: absolute; top: 14px; }
  .footer-col h5 { font-size: 12px; font-weight: 400; margin-bottom: 6px; }
  .footer-col p { font-size: 6px; line-height: 9px; color: #c8d0d8; display: flex; align-items: center; gap: 4px; }
  .social { display: flex; gap: 5px; }
  .social span { width: 13px; height: 13px; border-radius: 50%; border: 1.5px solid var(--white); }
  .copyright { position: absolute; top: 1183px; left: 0; width: 709px; height: 17px; background: var(--footer-deep); color: #aeb8c2; font-size: 5.5px; text-align: center; line-height: 17px; }
</style>
</head>
<body>

<header class="site-header">
  <div class="brand"><span class="brand-mark"></span><span class="brand-name">WachstumsBrücke Plus</span></div>
  <nav class="main-nav">
    <a class="active">HOME</a><a>ABOUT US</a><a>SERVICES</a><a>BLOG</a><a>CONTACT</a>
  </nav>
</header>

<section class="hero">
  <div class="hero-photo" role="img" aria-label="Photo of business people in a meeting around a table"></div>
  <div class="hero-shade"></div>
  <h1 class="hero-title">WE OFFER SERVICES TO SMALL AND MEDIUM SIZED COMPANIES</h1>
  <p class="hero-sub">WE SUPPORT YOUR TEAM IN LEADERSHIP, HEALTH AND FURTHER EDUCATION</p>
  <div class="hero-dots"><span></span><span></span><span class="on"></span></div>
</section>

<section class="about">
  <h2 class="section-title">ABOUT US</h2>
  <svg class="divider" width="60" height="8" viewBox="0 0 60 8"><line x1="0" y1="4" x2="25" y2="4" stroke="#c9c9c9" stroke-width="1"/><rect x="27" y="1" width="5" height="5" fill="#e57f2b" transform="rotate(45 29.5 3.5)"/><line x1="35" y1="4" x2="60" y2="4" stroke="#c9c9c9" stroke-width="1"/></svg>
  <p class="about-text">We are a consulting team for small and medium sized companies. With funded workshops and coaching over ten days we help owners and staff grow together. Our focus lies on leadership, on further education and on the health of your employees, because people are the true value of every company. We listen first, then build a plan that fits your daily work, your team and your goals, and we stay at your side until the changes work well in practice.</p>
</section>

<section class="workshops">
  <h2 class="section-title">OUR WORKSHOPS</h2>
  <svg class="divider" width="60" height="8" viewBox="0 0 60 8"><line x1="0" y1="4" x2="25" y2="4" stroke="#c9c9c9" stroke-width="1"/><rect x="27" y="1" width="5" height="5" fill="#e57f2b" transform="rotate(45 29.5 3.5)"/><line x1="35" y1="4" x2="60" y2="4" stroke="#c9c9c9" stroke-width="1"/></svg>

  <article class="workshop" style="left:74px">
    <svg width="96" height="96" viewBox="0 0 96 96" role="img" aria-label="Photo of a team discussing leadership"><defs><linearGradient id="g1" x1="0" y1="0" x2="1" y2="1"><stop offset="0" stop-color="#9fb4c6"/><stop offset="1" stop-color="#4d6175"/></linearGradient></defs><polygon points="48,2 88,25 88,71 48,94 8,71 8,25" fill="url(#g1)"/></svg>
    <h3>Leadership</h3>
    <p>Clear goals and good feedback help leaders guide their teams with trust and calm.</p>
    <span class="read-more">Read more</span>
  </article>

  <article class="workshop" style="left:274px">
    <svg width="96" height="96" viewBox="0 0 96 96" role="img" aria-label="Photo of a healthy employee at work"><defs><linearGradient id="g2" x1="0" y1="0" x2="1" y2="1"><stop offset="0" stop-color="#e3c9b6"/><stop offset="1" stop-color="#8b6d5c"/></linearGradient></defs><polygon points="48,2 88,25 88,71 48,94 8,71 8,25" fill="url(#g2)"/></svg>
    <h3>Employees Health</h3>
    <p>Healthy habits, less stress and a good workplace keep your staff strong and motivated.</p>
    <span class="read-more">Read more</span>
  </article>

  <article class="workshop" style="left:468px">
    <svg width="96" height="96" viewBox="0 0 96 96" role="img" aria-label="Photo of a group in a training session"><defs><linearGradient id="g3" x1="0" y1="0" x2="1" y2="1"><stop offset="0" stop-color="#c9d3de"/><stop offset="1" stop-color="#5a6b80"/></linearGradient></defs><polygon points="48,2 88,25 88,71 48,94 8,71 8,25" fill="url(#g3)"/></svg>
    <h3>Further Education</h3>
    <p>New skills open new chances, for every person and for the whole company alike.</p>
    <span class="read-more">Read more</span>
  </article>
</section>

<section class="mission">
  <p class="mission-text">Our work is dedicated to the prosperity of our clients!</p>
  <span class="mission-button">Click here</span>
</section>

<section class="testimonials">
  <h2 class="section-title">WHAT OUR AWESOME CLIENTS SAY ?</h2>
  <svg class="divider" width="60" height="8" viewBox="0 0 60 8"><line x1="0" y1="4" x2="25" y2="4" stroke="#c9c9c9" stroke-width="1"/><rect x="27" y="1" width="5" height="5" fill="#e57f2b" transform="rotate(45 29.5 3.5)"/><line x1="35" y1="4" x2="60" y2="4" stroke="#c9c9c9" stroke-width="1"/></svg>
  <p class="testimonials-intro">Owners and teams share how the workshops changed their daily work, their health and the way they lead.</p>

  <div class="testimonial-stage">
    <article class="testimonial" style="left:14px">
      <svg class="avatar" width="30" height="30" viewBox="0 0 30 30" role="img" aria-label="Portrait photo of the client"><circle cx="15" cy="15" r="14" fill="#8d9aa8" stroke="#fff" stroke-width="2"/></svg>
      <p>The workshops gave our team a clear plan. We now talk more openly, and our leaders feel sure about how to guide people every day.</p>
      <h4>Martin Kessler</h4><span>Consulting client</span>
    </article>
    <article class="testimonial" style="left:160px">
      <svg class="avatar" width="30" height="30" viewBox="0 0 30 30" role="img" aria-label="Portrait photo of the client"><circle cx="15" cy="15" r="14" fill="#7f8c99" stroke="#fff" stroke-width="2"/></svg>
      <p>Sick days went down and the mood went up. The health coaching was simple, practical and right for a small company like ours.</p>
      <h4>lena vogt</h4><span>Consulting client</span>
    </article>
    <article class="testimonial" style="left:306px">
      <svg class="avatar" width="30" height="30" viewBox="0 0 30 30" role="img" aria-label="Portrait photo of the client"><circle cx="15" cy="15" r="14" fill="#95a1ad" stroke="#fff" stroke-width="2"/></svg>
      <p>Thanks to the training our staff learned new skills fast. We can take on bigger projects now and we are proud of the result.</p>
      <h4>Paul Winter</h4><span>Consulting client</span>
    </article>
  </div>
</section>

<footer class="site-footer">
  <div class="footer-col" style="left:30px">
    <h5>Address</h5>
    <p>Kastanienweg 14</p><p>10437 Berlin</p><p>Germany</p>
  </div>
  <div class="footer-col" style="left:205px">
    <h5>Phones:</h5>
    <p><svg width="7" height="7" viewBox="0 0 10 10"><path d="M2 1 L4 1 L5 3 L4 4 Q5 6 6 6 L7 5 L9 6 L9 8 Q8 9 6 9 Q1 7 1 3 Q1 1 2 1Z" fill="#fff"/></svg>+49 30 555 0142</p>
    <p><svg width="7" height="7" viewBox="0 0 10 10"><path d="M2 1 L4 1 L5 3 L4 4 Q5 6 6 6 L7 5 L9 6 L9 8 Q8 9 6 9 Q1 7 1 3 Q1 1 2 1Z" fill="#fff"/></svg>+49 30 555 0187</p>
  </div>
  <div class="footer-col" style="left:400px">
    <h5>E-mail:</h5>
    <p>kontakt@wachstumsbruecke.example</p>
  </div>
  <div class="footer-col" style="left:560px">
    <h5>Follow Us</h5>
    <div class="social"><span></span><span></span><span></span></div>
  </div>
</footer>
<div class="copyright">Copyright © 2015 All rights reserved</div>

</body>
</html>
```